Business Card Design for Occupational Medicine Start Up Company

We need to design a professional business card. We are a healthcare company providing occupational medicine services to blue collar industries. We are professional, efficient and high quality service providers.

Target Market(s)

Blue Collar Industry: Shipbuilding, Ports, Trucking Companies; The Executives and Safety Officers for these companies

Industry/Entity Type

Healthcare

Contact Information for Business Card

Logo, Name, Title, Email, Phone

Other font styles liked:
• Please match our Brand Guide

Requirements
Must have
• Our Company Colors and Logo

```html
<!DOCTYPE html>
<html lang="en">
<head>
<meta charset="utf-8">
<title>CrewSafe Business Card</title>
<link rel="stylesheet" href="https://fonts.googleapis.com/css2?family=Source+Sans+3:wght@400;600&display=swap">
<style>
  :root {
    --backdrop: #b0b1b0;
    --card: #ffffff;
    --navy: #2b3480;
    --grey-text: #555a63;
    --accent: #f5c88a;
    --band-text: #ffffff;
  }
  * { box-sizing: border-box; margin: 0; padding: 0; }
  html, body {
    width: 1200px; height: 1200px; overflow: hidden;
    background: var(--backdrop);
    font-family: "Source Sans 3", sans-serif;
  }
  .card {
    position: absolute; left: 223px;
    width: 754px; height: 462px;
    background: var(--card);
    border-radius: 52px;
    overflow: hidden;
  }
  .card--front { top: 109px; }
  .card--back { top: 629px; }

  .brand {
    position: absolute;
    display: flex; align-items: center; gap: 12px;
    color: var(--navy); font-weight: 600;
    white-space: nowrap;
  }
  .brand__dot {
    display: block; border-radius: 50%;
    background: var(--navy);
  }
  .card--front .brand { left: 72px; top: 185px; font-size: 46px; }
  .card--front .brand__dot { width: 26px; height: 26px; }
  .card--back .brand { left: 50%; top: 50%; transform: translate(-50%, -50%); font-size: 58px; }
  .card--back .brand__dot { width: 32px; height: 32px; }

  .divider {
    position: absolute; left: 387px; top: 134px;
    width: 4px; height: 213px;
    background: var(--accent);
  }
  .person { position: absolute; left: 431px; top: 128px; }
  .person__name {
    color: var(--navy); font-weight: 600;
    font-size: 39px; line-height: 1.05;
  }
  .person__title {
    color: var(--grey-text); font-size: 23px; margin-top: 2px;
  }
  .contacts {
    position: absolute; left: 431px; top: 229px;
    list-style: none;
  }
  .contacts li {
    display: flex; align-items: center; gap: 10px;
    height: 31px;
    color: var(--grey-text); font-size: 21px;
  }
  .contacts svg { width: 21px; height: 21px; fill: var(--navy); flex: none; }
  .address-band {
    position: absolute; left: 0; right: 0; bottom: 0;
    height: 66px;
    background: var(--navy);
    color: var(--band-text);
    font-size: 23px;
    display: flex; align-items: center; justify-content: center;
  }
</style>
</head>
<body>
  <section class="card card--front">
    <div class="brand"><span class="brand__dot"></span>CrewSafe</div>
    <div class="divider"></div>
    <div class="person">
      <h1 class="person__name">Dana Whitfield</h1>
      <p class="person__title">Account Executive</p>
    </div>
    <ul class="contacts">
      <li>
        <svg viewBox="0 0 24 24" aria-hidden="true"><path d="M6.6 10.8a15.1 15.1 0 0 0 6.6 6.6l2.2-2.2c.3-.3.7-.4 1-.2 1.1.4 2.3.6 3.6.6.6 0 1 .4 1 1V20c0 .6-.4 1-1 1A17 17 0 0 1 3 4c0-.6.4-1 1-1h3.5c.6 0 1 .4 1 1 0 1.3.2 2.5.6 3.6.1.3 0 .7-.2 1z"/></svg>
        555.210.4830
      </li>
      <li>
        <svg viewBox="0 0 24 24" aria-hidden="true"><path d="M7 3h10v4H7zM4 8h16a2 2 0 0 1 2 2v6h-4v5H6v-5H2v-6a2 2 0 0 1 2-2zm4 7v4h8v-4z"/></svg>
        555.210.4831
      </li>
      <li>
        <svg viewBox="0 0 24 24" aria-hidden="true"><path d="M2 5h20v9.5a5 5 0 0 0-7 4.5H2zm2 2v.4l8 5 8-5V7l-8 5z"/><circle cx="19" cy="19" r="3.5"/></svg>
        dwhitfield@harborline.com
      </li>
      <li>
        <svg viewBox="0 0 24 24" aria-hidden="true"><path d="M12 2a10 10 0 1 0 0 20 10 10 0 0 0 0-20zm-1 2.1V8H7.6c.8-2 2-3.4 3.4-3.9zm2 0c1.4.5 2.6 1.9 3.4 3.9H13zM5.3 8h1.6c-.2.9-.3 1.9-.4 3H4.1c.2-1.1.6-2.1 1.2-3zm3.6 0H11v3H8.5c.1-1.1.2-2.1.4-3zM13 8h2.1c.2.9.3 1.9.4 3H13zm4.1 0h1.6c.6.9 1 1.9 1.2 3h-2.4c-.1-1.1-.2-2.1-.4-3zM4.1 13h2.4c.1 1.1.2 2.1.4 3H5.3c-.6-.9-1-1.9-1.2-3zm4.4 0H11v3H8.9c-.2-.9-.3-1.9-.4-3zm4.5 0h2.5c-.1 1.1-.2 2.1-.4 3H13zm4.5 0h2.4c-.2 1.1-.6 2.1-1.2 3h-1.6c.2-.9.3-1.9.4-3zM7.6 18H11v1.9c-1.4-.5-2.6-1.9-3.4-3.9zm5.4 0h3.4c-.8 2-2 3.4-3.4 3.9z"/></svg>
        www.harborline.com
      </li>
    </ul>
    <div class="address-band">48 Quarry Lane Suite 210 Portview, CA 90210</div>
  </section>

  <section class="card card--back">
    <div class="brand"><span class="brand__dot"></span>CrewSafe</div>
  </section>
</body>
</html>
```